Gym Membership Sales Sheet

I want this sheet to showcase the four contract types of bronze, silver, 6 month and platinum underneath of the three membership types of individual, partner and family. I am not particularly stuck on the bronze, silver, gold, platinum structure if you feel you have four better names that would work. However on the new sheet I want to remove the option for a 6 month contract. So, move up the PIF for just one year option and remove the three month option. Then remove everything else on the page. Add in hydromassage/tanning in with silver, gold and platinum contracts. The sheet needs to be simple.

Three membership types of individual, partner and family.

Then Bronze, silver, gold, platinum.

Silver, Gold and platinum members get hydromassage and tanning access. Only gold and platinum members get 15% of personal training and kinetics programs. Gold and Platinum members get free kid zone access as well.

Target Market(s)

Families, women and young adult males

Industry/Entity Type

Fitness

Colors
9bcb3c

Requirements
Must have
• Must have a cohesive design that highlights the membership types effectively. A design that is simple yet effective in causing people to choose Gold and Platinum plans. The goal of it is to up sell everyone into Gold and Platinum memberships.
Nice to have
• It would be nice to have three design types. One that appeals to women. One that appeals to young adult males and the third that appeals to families.
Should not have
• It should not be over complex and should not have a 6 month membership or 3 month membership options.

```html
<!DOCTYPE html>
<html lang="en">
<head>
<meta charset="utf-8">
<title>Northpeak Fitness – Membership Rate</title>
<link rel="stylesheet" href="https://fonts.googleapis.com/css2?family=Teko:wght@500&family=Roboto+Condensed:wght@400;700&family=Open+Sans:wght@400;700&display=swap">
<style>
:root{
  --green:#5a9e2f;
  --green-bright:#9bcb3c;
  --green-box-top:#6ab23a;
  --green-box-bottom:#4f9a28;
  --dark:#232323;
  --charcoal-top:#5a5a5a;
  --charcoal-bottom:#2b2b2b;
  --panel:#e9e8ea;
  --white:#ffffff;
  --ink:#1e1e1e;
  --silver-top:#f4f4f4;
  --silver-bottom:#c9c9c9;
  --gold-top:#f1c24a;
  --gold-bottom:#c98a12;
  --page:#ecebe8;
}
*{margin:0;padding:0;box-sizing:border-box}
html,body{width:1200px;height:1200px;overflow:hidden;background:var(--page)}
.sheet{
  position:absolute;left:172px;top:0;width:768px;height:1078px;
  transform:scale(1.1132);transform-origin:0 0;
  background:var(--white);font-family:"Open Sans",sans-serif;color:var(--ink);
}
.hero{position:absolute;left:0;top:0;width:768px;height:352px;
  background:linear-gradient(180deg,#ffffff 0%,#f3f5f7 40%,#dfe6ee 100%)}
.band-green{position:absolute;left:0;width:768px;background:var(--green)}
.band-dark{position:absolute;left:0;width:768px;background:var(--dark)}

.brand{position:absolute;left:50px;top:414px;display:flex;align-items:center;gap:8px;white-space:nowrap}
.brand-dot{width:18px;height:18px;border-radius:50%;background:var(--green);flex:none}
.brand-name{font-family:"Teko",sans-serif;font-weight:500;font-size:30px;line-height:1;color:var(--dark);letter-spacing:.5px}

.title{position:absolute;left:304px;top:399px;white-space:nowrap;font-family:"Teko",sans-serif;font-weight:500;font-size:70px;line-height:1;letter-spacing:0;color:var(--green)}
.title span{color:var(--dark)}

.rates{position:absolute;left:0;top:493px;width:768px;height:284px;background:var(--panel)}
.plan{position:absolute;top:505px;width:200px}
.plan-icon{position:absolute;left:0;top:0;width:50px;height:50px;border-radius:50%;background:var(--green)}
.plan-head{position:absolute;left:66px;top:2px;line-height:17px;white-space:nowrap}
.plan-type{font-weight:700;font-size:14px;color:var(--dark)}
.plan-word{font-weight:400;font-size:14px;color:var(--green)}
.plan-sub{font-size:10px;line-height:10px;color:var(--dark);font-weight:700;margin-top:1px}

.price-box{position:absolute;top:563px;width:191px;height:199px;color:var(--white);
  font-family:"Roboto Condensed",sans-serif;font-size:11px;box-shadow:0 8px 8px -6px rgba(0,0,0,.25)}
.price-box.green{background:linear-gradient(180deg,var(--green-box-top),var(--green-box-bottom))}
.price-box.charcoal{background:linear-gradient(180deg,var(--charcoal-top),var(--charcoal-bottom))}
.row{position:absolute;left:16px;right:12px;display:flex;align-items:flex-end}
.row .label{line-height:15px}
.row .dots{flex:1;border-bottom:1px dotted rgba(255,255,255,.8);margin:0 3px 4px}
.row .amount{font-size:13px;color:var(--dark)}
.charcoal .row .amount{color:var(--green-bright)}
.divider{position:absolute;left:58px;width:76px;top:141px;border-top:1px solid var(--dark)}
.charcoal .divider{border-color:var(--green-bright)}
.note{position:absolute;left:0;right:0;top:153px;text-align:center;line-height:15px}

.pif-bar{position:absolute;width:191px;height:34px;display:flex;align-items:center;justify-content:center;white-space:nowrap;
  font-family:"Roboto Condensed",sans-serif;font-size:12.5px;color:var(--dark);text-transform:uppercase}
.pif-bar.silver{top:794px;background:linear-gradient(180deg,var(--silver-top),var(--silver-bottom));border:1px solid #a8a8a8}
.pif-bar.gold{top:882px;background:linear-gradient(180deg,var(--gold-top),var(--gold-bottom));border:1px solid #a36d0a}
.pif-bar .accent{color:var(--green);margin:0 3px}
.pif-bar.gold .accent{color:var(--white)}
.pif-line{position:absolute;display:flex;align-items:center;gap:6px;white-space:nowrap;font-family:"Roboto Condensed",sans-serif;font-size:11px;color:var(--dark)}
.tick{width:12px;height:12px;flex:none}

.perks{position:absolute;left:0;top:965px;width:768px;height:90px;background:var(--panel)}
.perk{position:absolute;top:992px;display:flex;gap:6px;white-space:nowrap;font-family:"Roboto Condensed",sans-serif;font-size:10.5px;line-height:15px;color:var(--dark)}
.perk .tick{margin-top:2px}
.perk-sep{position:absolute;top:992px;width:1px;height:40px;background:var(--dark)}
</style>
</head>
<body>
<svg width="0" height="0" style="position:absolute">
  <symbol id="tick" viewBox="0 0 12 12"><circle cx="6" cy="6" r="5.2" fill="none" stroke="#5a9e2f" stroke-width="1.2"/><path d="M3.4 6.2l1.8 1.8 3.6-3.8" fill="none" stroke="#5a9e2f" stroke-width="1.4"/></symbol>
  <symbol id="person" viewBox="0 0 50 50"><circle cx="25" cy="12" r="4" fill="#fff"/><path d="M19 18h12v13h-3v12h-6V31h-3z" fill="#fff"/></symbol>
  <symbol id="pair" viewBox="0 0 50 50"><circle cx="19" cy="12" r="3.6" fill="#fff"/><path d="M14 18h10v12h-2.5v12h-5V30H14z" fill="#fff"/><circle cx="32" cy="12" r="3.6" fill="#fff"/><path d="M27 18h10v12h-2.5v12h-5V30H27z" fill="#fff"/></symbol>
  <symbol id="family" viewBox="0 0 50 50"><circle cx="13" cy="13" r="3.4" fill="#fff"/><path d="M9 19h8v11h-2v11h-4V30H9z" fill="#fff"/><circle cx="37" cy="13" r="3.4" fill="#fff"/><path d="M33 19h8l1 11h-2v11h-4V30h-2z" fill="#fff"/><circle cx="22" cy="23" r="2.4" fill="#fff"/><path d="M19.5 27h5v7h-1.5v7h-2v-7h-1.5z" fill="#fff"/><circle cx="28" cy="23" r="2.4" fill="#fff"/><path d="M25.5 27h5v7h-1.5v7h-2v-7h-1.5z" fill="#fff"/></symbol>
</svg>

<main class="sheet">
  <div class="hero" role="img" aria-label="Group photo of smiling gym members of all ages in workout clothes, holding dumbbells, a ball and water bottles"></div>
  <div class="band-green" style="top:352px;height:8px"></div>
  <div class="band-dark" style="top:360px;height:3px"></div>

  <div class="brand"><span class="brand-dot"></span><span class="brand-name">NORTHPEAK FITNESS</span></div>
  <h1 class="title">MEMBERSHIP <span>RATE</span></h1>

  <section class="rates"></section>

  <div class="plan" style="left:46px">
    <svg class="plan-icon"><use href="#person"/></svg>
    <div class="plan-head"><div class="plan-type">INDIVIDUAL</div><div class="plan-word">MEMBERSHIPS</div><div class="plan-sub">One Adult 18+</div></div>
  </div>
  <div class="plan" style="left:280px">
    <svg class="plan-icon"><use href="#pair"/></svg>
    <div class="plan-head"><div class="plan-type">PARTNER</div><div class="plan-word">MEMBERSHIPS</div><div class="plan-sub">Two Adults</div></div>
  </div>
  <div class="plan" style="left:514px">
    <svg class="plan-icon"><use href="#family"/></svg>
    <div class="plan-head" style="left:68px"><div class="plan-type">FAMILY</div><div class="plan-word">MEMBERSHIPS</div><div class="plan-sub">2 Adults, 2 Children<br>Ages 13-17</div></div>
  </div>

  <div class="price-box green" style="left:47px">
    <div class="row" style="top:20px"><span class="label">Bronze Membership</span><span class="dots"></span><span class="amount">$49.99</span></div>
    <div class="row" style="top:45px"><span class="label">Gold 12 Months<br>Contract</span><span class="dots"></span><span class="amount">$69.99</span></div>
    <div class="row" style="top:85px"><span class="label">Platinum 18 Months<br>Contract</span><span class="dots"></span><span class="amount">$59.99</span></div>
    <div class="divider"></div>
    <p class="note">(Also Includes 15% off Personal Training<br>&amp; Kinetics Programs)</p>
  </div>
  <div class="price-box charcoal" style="left:281px">
    <div class="row" style="top:20px"><span class="label">Bronze Membership</span><span class="dots"></span><span class="amount">$69.99</span></div>
    <div class="row" style="top:45px"><span class="label">Gold 12 Months<br>Contract</span><span class="dots"></span><span class="amount">$89.99</span></div>
    <div class="row" style="top:85px"><span class="label">Platinum 18 Months<br>Contract</span><span class="dots"></span><span class="amount">$79.99</span></div>
    <div class="divider"></div>
    <p class="note">(Also Includes 15% off Personal Training<br>&amp; Kinetics Programs)</p>
  </div>
  <div class="price-box green" style="left:515px">
    <div class="row" style="top:20px"><span class="label">Bronze Membership</span><span class="dots"></span><span class="amount">$79.99</span></div>
    <div class="row" style="top:45px"><span class="label">Gold 12 Months<br>Contract</span><span class="dots"></span><span class="amount">$99.99</span></div>
    <div class="row" style="top:85px"><span class="label">Platinum 18 Months<br>Contract</span><span class="dots"></span><span class="amount">$89.99</span></div>
    <div class="divider"></div>
    <p class="note">(Also Includes 15% off Personal Training<br>&amp; Kinetics Programs)</p>
  </div>

  <div class="pif-bar silver" style="left:47px">Silver<span class="accent">Individual</span>Paid in Full</div>
  <div class="pif-bar silver" style="left:282px">Silver<span class="accent">Partner</span>Paid in Full</div>
  <div class="pif-bar silver" style="left:515px">Silver<span class="accent">Family</span>Paid in Full</div>
  <div class="pif-line" style="left:66px;top:844px"><svg class="tick"><use href="#tick"/></svg>1 Year - $480.00 ($40/mo)</div>
  <div class="pif-line" style="left:300px;top:843px"><svg class="tick"><use href="#tick"/></svg>1 Year- $660 ($55/mo)</div>
  <div class="pif-line" style="left:542px;top:840px"><svg class="tick"><use href="#tick"/></svg>1 Year - $840.00 ($70/mo)</div>

  <div class="pif-bar gold" style="left:47px">Gold Individual Paid in Full</div>
  <div class="pif-bar gold" style="left:282px">Gold Partner Paid in Full</div>
  <div class="pif-bar gold" style="left:514px">Gold<span class="accent">Family</span>Paid in Full</div>
  <div class="pif-line" style="left:66px;top:931px"><svg class="tick"><use href="#tick"/></svg>1 Year $720 ($60/mo)</div>
  <div class="pif-line" style="left:300px;top:931px"><svg class="tick"><use href="#tick"/></svg>1 Year- $900 ($75/mo)</div>
  <div class="pif-line" style="left:542px;top:930px"><svg class="tick"><use href="#tick"/></svg>1 Year- $1080 ($90/mo)</div>

  <section class="perks"></section>
  <div class="perk" style="left:47px"><svg class="tick"><use href="#tick"/></svg><p>Silver, Gold and platinum members<br>get hydromassage &amp; tanning access.</p></div>
  <div class="perk-sep" style="left:259px"></div>
  <div class="perk" style="left:306px"><svg class="tick"><use href="#tick"/></svg><p>Gold and Platinum members<br>get free kid zone access as well</p></div>
  <div class="perk-sep" style="left:509px"></div>
  <div class="perk" style="left:557px"><svg class="tick"><use href="#tick"/></svg><p>Only gold and platinum members<br>get 15% of personal training and<br>kinetics programs.</p></div>

  <div class="band-dark" style="top:1055px;height:3px"></div>
  <div class="band-green" style="top:1058px;height:20px"></div>
</main>
</body>
</html>
```